Event flyer for Sunday night Youth Group

Need a 4 x 6 or 5 x 7 flyer for a new youth group starting on April 14. The youth group is for students in middle school and high school so it needs to look fun and cool, but not childish. I prefer it not to include pictures of people unless it's so obscure you can't really see their faces. I've uploaded some pictures of flyers I like. I've also attached a couple versions of our logo to use on the flyer.
Information the flyer needs to include:
Youth Group
Sundays, 6-8pm (beginning April 14)
Location: Merriwick's - 4219 Hollowfern Ln S, Keizer, 97418
There will be dinner, games, friends, and a message.
Target Market(s)
Youth ages 13-18
Industry/Entity Type
Church
Colors
Designer to choose colors to be used in the design.
Look and feel

```html
<!DOCTYPE html>
<html lang="en">
<head>
<meta charset="utf-8">
<title>Youth Group – Sunday Nights</title>
<link rel="stylesheet" href="https://fonts.googleapis.com/css2?family=Pinyon+Script&family=Poppins:wght@400;500;600;700;800&display=swap">
<style>
  :root{
    --ink:#10212a;
    --ink-deep:#0b171e;
    --ink-soft:#1d3540;
    --sage:#808c7c;
    --teal:#4f7f92;
    --white:#ffffff;
    --frame:#8f9a88;
    --pin:#e0202e;
    --ghost:rgba(255,255,255,.24);
  }
  html,body{margin:0;padding:0;overflow:hidden;background:var(--ink-deep);}
  .flyer{
    position:relative;width:847px;height:1200px;overflow:hidden;
    background:radial-gradient(ellipse at 50% 25%, var(--ink-soft) 0%, var(--ink) 55%, var(--ink-deep) 100%);
    font-family:"Poppins",sans-serif;color:var(--white);
  }
  .crowd{
    position:absolute;left:0;right:0;top:470px;height:730px;
    background:linear-gradient(180deg, rgba(16,33,42,0) 0%, rgba(34,56,66,.55) 35%, rgba(26,46,56,.6) 70%, rgba(11,23,30,.9) 100%);
  }
  .frame{position:absolute;border:1px solid var(--frame);pointer-events:none;}
  .frame--outer{inset:18px;}
  .frame--inner{inset:24px;}

  .brand{
    position:absolute;top:92px;left:0;right:0;display:flex;justify-content:center;align-items:center;gap:14px;
  }
  .brand__mark{width:14px;height:14px;background:var(--white);}
  .brand__name{font-weight:400;font-size:28px;letter-spacing:2px;line-height:1;color:var(--white);}

  .title{margin:0;}
  .title-script{
    position:absolute;top:200px;left:0;right:0;text-align:center;
    font-family:"Pinyon Script",cursive;font-size:128px;line-height:1.1;color:var(--white);
    text-shadow:0 0 8px rgba(255,255,255,.6),0 0 18px rgba(255,255,255,.3);
    z-index:3;
  }
  .group-stack{position:absolute;left:112px;top:364px;width:630px;height:412px;overflow:visible;z-index:2;}
  .group-stack text{font-family:"Poppins",sans-serif;font-weight:800;font-size:180px;}
  .group--solid{fill:var(--sage);}
  .group--echo{fill:none;stroke:var(--ghost);stroke-width:1.2;}
  .group--echo-2{opacity:.7;}

  .beginning{
    position:absolute;top:676px;left:0;right:0;margin:0;text-align:center;
    font-family:"Pinyon Script",cursive;font-size:66px;line-height:1;color:var(--white);
    text-shadow:0 0 6px rgba(255,255,255,.4);z-index:3;
  }

  .date{position:absolute;left:0;top:0;width:100%;height:100%;pointer-events:none;}
  .date__day{position:absolute;left:206px;top:766px;font-weight:600;font-size:164px;line-height:1;letter-spacing:-8px;}
  .date__month{position:absolute;left:372px;top:786px;font-weight:700;font-size:62px;line-height:1;color:var(--teal);letter-spacing:-1px;}
  .date__weekday{position:absolute;left:374px;top:842px;font-weight:500;font-size:27px;letter-spacing:6.5px;line-height:1;}
  .date__time{position:absolute;left:377px;top:879px;width:177px;height:26px;background:var(--sage);color:var(--ink);font-weight:700;font-size:20px;line-height:26px;text-align:center;}
  .date__year{
    position:absolute;left:578px;top:793px;border:1px solid var(--white);height:110px;width:34px;box-sizing:border-box;
    display:flex;align-items:center;justify-content:center;
    writing-mode:vertical-rl;font-size:19px;letter-spacing:7px;font-weight:400;line-height:1;
  }

  .venue{
    position:absolute;top:934px;left:0;right:0;margin:0;display:flex;justify-content:center;align-items:center;gap:8px;
    font-weight:700;font-size:18px;line-height:24px;
  }
  .venue svg{width:15px;height:19px;}

  .extras-heading{
    position:absolute;top:1010px;left:0;right:0;margin:0;text-align:center;
    font-weight:500;font-size:18px;line-height:24px;letter-spacing:8px;color:var(--sage);
  }
  .extras{position:absolute;top:1048px;left:0;right:0;height:80px;}
  .extra{position:absolute;width:150px;text-align:center;transform:translateX(-50%);font-size:17px;line-height:22px;}
  .extra svg{display:block;margin:0 auto 4px;width:42px;height:38px;fill:none;stroke:var(--teal);stroke-width:1.8;stroke-linecap:round;stroke-linejoin:round;}
  .extra--dinner{left:174px;}
  .extra--games{left:317px;}
  .extra--friends{left:474px;}
  .extra--message{left:646px;}
</style>
</head>
<body>
<main class="flyer">
  <div class="crowd" role="img" aria-label="Dim silhouetted crowd of young people at a gathering, softly faded into the background"></div>
  <div class="frame frame--outer"></div>
  <div class="frame frame--inner"></div>

  <header class="brand">
    <span class="brand__mark"></span>
    <span class="brand__name">WAYPOINT FELLOWSHIP</span>
  </header>

  <h1 class="title">
    <span class="title-script">Youth</span>
    <svg class="group-stack" viewBox="0 0 630 412" aria-label="GROUP">
      <text class="group--echo group--echo-2" x="4" y="408" textLength="622" lengthAdjust="spacingAndGlyphs" aria-hidden="true">GROUP</text>
      <text class="group--echo" x="4" y="270" textLength="622" lengthAdjust="spacingAndGlyphs" aria-hidden="true">GROUP</text>
      <text class="group--solid" x="4" y="132" textLength="622" lengthAdjust="spacingAndGlyphs">GROUP</text>
    </svg>
  </h1>

  <p class="beginning">Beginning</p>

  <div class="date">
    <span class="date__day">14</span>
    <span class="date__month">APRIL</span>
    <span class="date__weekday">SUNDAY</span>
    <span class="date__time">6PM - 8PM</span>
    <span class="date__year">2024</span>
  </div>

  <p class="venue">
    <svg viewBox="0 0 16 20" aria-hidden="true"><path d="M8 0C3.6 0 0 3.4 0 7.6 0 13 8 20 8 20s8-7 8-12.4C16 3.4 12.4 0 8 0z" fill="var(--pin)"/><circle cx="8" cy="7.5" r="3" fill="var(--white)"/></svg>
    Merriwick's - 4219 Hollowfern Ln S, Keizer, 97418
  </p>

  <p class="extras-heading">THERE WILL BE</p>
  <div class="extras">
    <div class="extra extra--dinner">
      <svg viewBox="0 0 44 40" aria-hidden="true"><circle cx="23" cy="22" r="12"/><circle cx="23" cy="22" r="7"/><path d="M6 6v10M3 6v7c0 2 1.5 3 3 3s3-1 3-3V6M6 16v20"/><path d="M40 6c-3 2-4 7-4 13h4v17"/></svg>
      Dinner
    </div>
    <div class="extra extra--games">
      <svg viewBox="0 0 44 40" aria-hidden="true"><rect x="20" y="4" width="16" height="22" rx="2" transform="rotate(15 28 15)"/><path d="M8 36h16M10 36l2-8h8l2 8M12 28c-2-4 0-9 4-10 3 1 5 4 4 10"/></svg>
      Games
    </div>
    <div class="extra extra--friends">
      <svg viewBox="0 0 44 40" aria-hidden="true"><circle cx="12" cy="18" r="4"/><circle cx="22" cy="18" r="4"/><circle cx="32" cy="18" r="4"/><path d="M5 34c0-6 3-9 7-9s7 3 7 9M15 34c0-6 3-9 7-9s7 3 7 9M25 34c0-6 3-9 7-9s7 3 7 9"/><path d="M22 11c-3-3-6-5-6-8 0-2 3-3 6 0 3-3 6-2 6 0 0 3-3 5-6 8z"/></svg>
      Friends
    </div>
    <div class="extra extra--message">
      <svg viewBox="0 0 44 40" aria-hidden="true"><path d="M4 12c3-5 8-6 12-2l6 6 6-6c4-4 9-3 12 2M4 12l8 12M40 12l-8 12"/><path d="M12 24c3 4 6 6 10 6s7-2 10-6"/><path d="M18 18l4 4 4-4"/></svg>
      &amp; a message
    </div>
  </div>
</main>
</body>
</html>
```